Kettle Ledger Business Card design

We need a stand out business card design for Accounting practice based in Australia specialising in pubs, clubs and hotels. We help venues maximise margins, create time and manage cashflow. One club we have been working with for the last 6 months has increased revenue by 3% and margin by 5% in this time frame. We have a back office outsourced system that costs less than having a full time employee and also allows the venues the added benefit of:<br/>-using the office space to become a revenue generating opportunity. <br/>-a complete system to enhance governance, accountability and efficiency within their operation<br/>-52 weeks cover so no hassle to cover annual/sick .. leave<br/><br/>We would like to see designs that use the colours of our logo (green & blue).
Target Market(s)
Australian Pubs, Clubs & Hotels abookkeeping, accounting and tax services
Industry/Entity Type
Accountant
Contact Information for Business Card
Miriam Oakley CPA
Principal
Accountant Tax Agent
Miriam@KettleLedger-example.com.au
0418693142
www.kettleledger-example.com.au
Accounting / Payroll / Tax / SMSF / Technology
Colors
Designer to choose colors to be used in the design.
Look and feel
Each slider illustrates characteristics of the customer's brand and the style your logo design should communicate.

```html
<!DOCTYPE html>
<html lang="en">
<head>
<meta charset="utf-8">
<title>Kettle Ledger Business Card</title>
<link href="https://fonts.googleapis.com/css2?family=Montserrat:wght@700;800&family=Open+Sans:wght@400;600&display=swap" rel="stylesheet">
<style>
  :root {
    --bg: #262626;
    --green: #0f7340;
    --green-line: #1a7a45;
    --blue: #233f8f;
    --white: #ffffff;
    --ink: #1c1c1c;
    --partner-blue: #1f5fa8;
    --partner-yellow: #f5cf1b;
    --partner-lime: #b6d32f;
    --partner-grey: #3a3a3a;
  }
  * { box-sizing: border-box; margin: 0; padding: 0; }
  html, body { width: 1200px; height: 900px; overflow: hidden; background: var(--bg); }
  body { position: relative; font-family: "Open Sans", Arial, sans-serif; color: var(--ink); }

  .card {
    position: absolute; left: 260px; width: 680px; height: 388px;
    background: var(--white); overflow: hidden;
    box-shadow: 0 12px 30px rgba(0,0,0,.5);
  }
  .card--front { top: 42px; }
  .card--back { top: 470px; }

  /* Front */
  .front-band {
    position: absolute; left: 0; top: 0; width: 100%; height: 246px;
    background: var(--green);
    display: flex; align-items: center; justify-content: center; gap: 22px;
  }
  .front-stripe {
    position: absolute; left: 0; top: 256px; width: 100%; height: 7px;
    background: var(--green);
  }
  .brand { display: flex; align-items: center; gap: 18px; }
  .brand-dot { border-radius: 50%; flex: none; }
  .brand-name {
    font-family: "Montserrat", Arial, sans-serif; font-weight: 800;
    color: var(--white); letter-spacing: .5px; white-space: nowrap;
  }
  .front-band .brand-dot { width: 70px; height: 70px; background: var(--white); }
  .front-band .brand-name { font-size: 56px; }

  .partners {
    position: absolute; left: 0; top: 263px; width: 100%; height: 125px;
    display: flex; align-items: center; justify-content: space-between;
    padding: 0 48px 0 52px;
  }
  .partner-block { display: flex; width: 210px; height: 84px; }
  .partner-block__left { flex: 1.6; background: var(--partner-blue); }
  .partner-block__right { flex: 1; background: var(--partner-yellow); }
  .partner-registered { display: flex; align-items: center; gap: 14px; }
  .partner-circle {
    width: 82px; height: 82px; border-radius: 50%;
    border: 2px solid var(--partner-grey); background: var(--white);
    display: flex; align-items: center; justify-content: center;
  }
  .partner-circle span { width: 46px; height: 46px; border-radius: 50%; background: var(--partner-lime); display: block; }
  .agent-number { font-size: 13px; line-height: 1.1; color: var(--ink); }
  .partner-square { width: 120px; height: 70px; border: 2px solid var(--partner-grey); }

  /* Back */
  .back-band {
    position: absolute; left: 0; top: 0; width: 100%; height: 186px;
    background: var(--blue);
    display: flex; align-items: center; justify-content: center;
  }
  .back-band .brand-dot { width: 64px; height: 64px; background: var(--green); }
  .back-band .brand-name { font-size: 50px; }
  .back-rule {
    position: absolute; left: 22px; right: 22px; top: 206px; height: 2px;
    background: var(--green-line);
  }
  .identity { position: absolute; left: 24px; top: 226px; width: 300px; text-align: right; }
  .identity__name {
    font-family: "Montserrat", Arial, sans-serif; font-weight: 700;
    font-size: 25px; color: var(--blue); white-space: nowrap;
  }
  .identity__role { font-size: 16px; white-space: nowrap; margin-top: 2px; }
  .sep { color: var(--green); font-weight: 600; padding: 0 4px; }
  .divider {
    position: absolute; left: 340px; top: 228px; width: 2px; height: 70px;
    background: var(--green-line);
  }
  .contacts { position: absolute; left: 354px; top: 226px; list-style: none; }
  .contacts li { display: flex; align-items: center; gap: 9px; font-size: 15.5px; line-height: 24px; white-space: nowrap; }
  .contacts svg { width: 17px; height: 17px; flex: none; }
  .web-domain { color: var(--green); }
  .services {
    position: absolute; left: 0; right: 0; top: 322px;
    text-align: center; font-size: 20px; white-space: nowrap;
  }
</style>
</head>
<body>

<section class="card card--front" aria-label="Business card front">
  <div class="front-band">
    <div class="brand">
      <span class="brand-dot"></span>
      <span class="brand-name">Kettle Ledger</span>
    </div>
  </div>
  <div class="front-stripe"></div>
  <div class="partners">
    <div class="partner-block" role="img" aria-label="Professional accounting body membership badge">
      <span class="partner-block__left"></span><span class="partner-block__right"></span>
    </div>
    <div class="partner-registered">
      <div class="partner-circle" role="img" aria-label="Registered tax practitioner badge"><span></span></div>
      <p class="agent-number">Tax agent<br>10482736</p>
    </div>
    <div class="partner-square" role="img" aria-label="Chartered tax adviser membership badge"></div>
  </div>
</section>

<section class="card card--back" aria-label="Business card back">
  <div class="back-band">
    <div class="brand">
      <span class="brand-dot"></span>
      <span class="brand-name">Kettle Ledger</span>
    </div>
  </div>
  <div class="back-rule"></div>

  <div class="identity">
    <p class="identity__name">Miriam Oakley CPA</p>
    <p class="identity__role">Principal<span class="sep">|</span>Accountant Tax Agent</p>
  </div>
  <div class="divider"></div>

  <ul class="contacts">
    <li>
      <svg viewBox="0 0 24 24" fill="none" stroke="#0f7340" stroke-width="2" aria-hidden="true"><path d="M5 3h4l2 5-2.5 1.5a11 11 0 0 0 6 6L16 13l5 2v4a2 2 0 0 1-2 2A16 16 0 0 1 3 5a2 2 0 0 1 2-2z"/></svg>
      041-869-3142
    </li>
    <li>
      <svg viewBox="0 0 24 24" fill="none" stroke="#0f7340" stroke-width="2" aria-hidden="true"><rect x="3" y="5" width="18" height="14"/><path d="M3 5l9 8 9-8"/></svg>
      Miriam@KettleLedger-example.com.au
    </li>
    <li>
      <svg viewBox="0 0 24 24" fill="none" stroke="#0f7340" stroke-width="2" aria-hidden="true"><circle cx="12" cy="12" r="9"/><path d="M3 12h18M12 3c3 3 3 15 0 18M12 3c-3 3-3 15 0 18"/></svg>
      <span>www.<span class="web-domain">kettleledger-example</span>.com.au</span>
    </li>
  </ul>

  <p class="services">Accounting<span class="sep">|</span>Payroll<span class="sep">|</span>Tax<span class="sep">|</span>SMSF<span class="sep">|</span>Technology</p>
</section>

</body>
</html>
```